We are growing our coaching practice and need some help creating collateral

Our organisation is building a coaching practice. It's going well and we want to take it to the next level. To date, we've done our own basic marketing material (attached), but now we want to create something more substantial that captures our approach and gives us confidence and pride when talking to customers. Things to note - we aren't looking for logo design, that's a separate branding discussion in our organisation. We are looking for someone to take our existing content and make it look good - this might be in the form of a flyer or PPT slide deck for example.
The format we are looking for is the offering title - in this case, 'Coaching', a brief description, and then some further detail.
Target Market(s)
Corporate, Healthcare, IT
Colors
Designer to choose colors to be used in the design.
Look and feel
Each slider illustrates characteristics of the customer's brand and the style your logo design should communicate.

```html
<!DOCTYPE html>
<html lang="en">
<head>
<meta charset="utf-8">
<title>Harbourline Executive Coaching</title>
<link href="https://fonts.googleapis.com/css2?family=Barlow+Condensed:wght@300;400;500;600;700&display=swap" rel="stylesheet">
<style>
  :root{
    --ink:#1c1c1c;
    --text:#333333;
    --orange:#e06a28;
    --red:#ee3e24;
    --panel-grey:#f3f2f4;
    --page:#000000;
    --white:#ffffff;
  }
  *{margin:0;padding:0;box-sizing:border-box}
  html,body{width:1200px;height:1200px;overflow:hidden;background:var(--page)}
  body{font-family:"Barlow Condensed",sans-serif;color:var(--text)}
  .flyer{position:absolute;left:144px;top:0;width:922px;height:1200px;background:var(--white);overflow:hidden}

  .hero{position:absolute;left:0;top:0;width:922px;height:490px}
  .hero svg{display:block}
  .brand{position:absolute;left:28px;top:44px;font-size:38px;font-weight:400;color:var(--ink);letter-spacing:.5px}
  .hero-headline{position:absolute;left:40px;top:224px;width:480px;
    font-size:36px;font-weight:300;line-height:42px;color:var(--white);white-space:nowrap}
  .hero-headline strong{font-weight:600;color:var(--ink)}

  .intro{position:absolute;left:0;top:490px;width:922px;height:376px}
  .intro-left{position:absolute;left:0;top:0;width:462px;height:376px;background:var(--white)}
  .intro-right{position:absolute;left:462px;top:0;width:460px;height:376px;background:var(--panel-grey)}
  .section-title{position:absolute;left:40px;top:20px;font-size:30px;font-weight:500;color:var(--red);white-space:nowrap}
  .section-title b{font-weight:700}
  .title-rule{position:absolute;left:40px;top:67px;width:246px;height:2px;background:var(--ink)}
  .title-rule::before{content:"";position:absolute;left:0;top:-1px;width:50px;height:4px;background:var(--orange)}
  .body-copy{font-size:18px;line-height:27px;font-weight:400;color:var(--text);text-align:justify}
  .body-copy b{font-weight:600;color:var(--ink)}
  .copy-a{position:absolute;left:40px;top:90px;width:384px}
  .divider{position:absolute;left:40px;top:220px;width:384px;border-top:1px dashed #777}
  .copy-b{position:absolute;left:40px;top:242px;width:384px}
  .copy-c{position:absolute;left:40px;top:30px;width:384px}
  .copy-d{position:absolute;left:40px;top:190px;width:384px}

  .offer{position:absolute;left:0;top:866px;width:922px;height:272px;background:var(--red);
    color:var(--white);text-align:center;font-size:27px;line-height:42.5px;font-weight:400;padding-top:30px;white-space:nowrap}
  .offer strong{font-weight:700;color:var(--ink)}

  .contact{position:absolute;left:0;top:1138px;width:922px;height:62px;display:flex;align-items:center;justify-content:center;
    font-size:25px;font-weight:500;color:var(--ink)}
</style>
</head>
<body>
<main class="flyer">
  <header class="hero">
    <svg width="922" height="490" viewBox="180 0 1153 612" preserveAspectRatio="none" xmlns="http://www.w3.org/2000/svg">
      <defs>
        <linearGradient id="bridgeSky" x1="0" y1="0" x2="0" y2="1">
          <stop offset="0" stop-color="#aab8c6"/>
          <stop offset="0.5" stop-color="#8ea3b7"/>
          <stop offset="1" stop-color="#3f6f93"/>
        </linearGradient>
        <linearGradient id="bridgeGlow" x1="0" y1="0" x2="1" y2="0">
          <stop offset="0" stop-color="#e0552a" stop-opacity="0"/>
          <stop offset="0.55" stop-color="#e0552a" stop-opacity=".55"/>
          <stop offset="1" stop-color="#e0552a" stop-opacity=".1"/>
        </linearGradient>
      </defs>
      <g role="img" aria-label="Photo of a large red suspension bridge over a bay with a city skyline behind">
        <polygon points="645,0 1333,0 1333,612 280,612" fill="url(#bridgeSky)"/>
        <polygon points="645,0 1333,0 1333,612 280,612" fill="url(#bridgeGlow)"/>
      </g>
      <polygon points="180,180 428,180 456,260 180,260" fill="var(--red)"/>
      <polygon points="180,260 688,260 895,612 180,612" fill="var(--orange)"/>
    </svg>
    <div class="brand">Harbourline</div>
    <h1 class="hero-headline">Why not <strong>explore</strong> the<br>possibilities executive<br>coaching offers through<br>a no obligation <strong>initial session</strong>,<br>ensuring the approach and the<br>coach is a <strong>good fit for you?</strong></h1>
  </header>

  <section class="intro">
    <div class="intro-left">
      <h2 class="section-title"><b>Harbourline</b> Executive Coaching</h2>
      <div class="title-rule"></div>
      <p class="body-copy copy-a">We believe great coaching is a bridge: one that enables you to see more clearly and cross the unexpected chasms; one that supports and challenges your thinking and actions to progress your significant goals.</p>
      <div class="divider"></div>
      <p class="body-copy copy-b">We build a creative and confidential partnership with you, one that is grounded in the science of leadership, change and coaching psychology so that practical results are an expectation and not left to chance.</p>
    </div>
    <div class="intro-right">
      <p class="body-copy copy-c"><b>Our coaches</b> are highly attuned to the human systems within which you work and live, since understanding those interconnected forces is vital to unlock movement. We build on your existing strengths and seek sustainable shifts, ones that create ripple effects of positive change.</p>
      <p class="body-copy copy-d"><b>Leaders</b> every where face unprecedented change, pressure, ambiguity, culture and accountability dilemmas. And yet every leader also has a different story, different terrain to navigate and different aspirations. This is where executive coaching with <b>Harbourline</b> can create extraordinary results.</p>
    </div>
  </section>

  <section class="offer">
    <p>“ Our coaching packages typically consist of blocks of <strong>7 hourly sessions,</strong><br>
    conducted fortnightly (with flexibility to customise)<br>
    For <strong>EL2 leaders</strong>, the investment in a block of <strong>7 sessions is $3400 + GST.</strong><br>
    This includes significant preparation and conceptualisation time before &amp;<br>
    after sessions by your coach to ensure you <strong>achieve maximum value.</strong> ”</p>
  </section>

  <footer class="contact">Contact Sam Hollis, ph. 0400 xxxxxx, sam.hollis@harbourline.com</footer>
</main>
</body>
</html>
```